Building company with a modern and unique product looking for a business card to help us stand out

We currently have a logo but as our business has grown, we feel that our business card is not reflecting our modern and high quality product and help us stand out from the crowd. Our business is mainly in the construction of new homes using a unique method and materials that makes our homes fire proof, vermin and pest resistant and rated to the maximum cyclone category (category 5). We need a business card that helps us stand out as well as communicating professionalism, high quality and trustworthiness. I have attached our current logo with a black and white option, as well as our business card which is double sided. We would like to retain as much of the information that is currently on our business cards, but presented in a more sleek way. We do like our current colour palette ( white, black, yellow and grey) and have been looking primarily at business cards with a black background however we are open to other combinations of colour and layout as long as we stand out. Please feel free to tweak our logo to make it more suitable for a business card, we like the black option that we use but we have had trouble trying to get the white area to match the rest of the logo and blend effectively into a business card. Please do not hesitate to contact us with any questions as we really want this to be successful!

Target Market(s)

Large contracts including government and larger companies

Industry/Entity Type

Business

We will be providing this business card to potential clients including key government ministers and large funding companies, our business card should show that we are professional and reliable.

Requirements
Must have
• It must be easy to read and pleasing to the eye, It must contain as much of the information on the current business card and unless something really stands out, we will most likely pick a design that has all of the information included. It must include our logo of course and have some colour included.
Nice to have
• We are looking for a high end business card and would like to see designs that reflect this. We like the gloss/matte contrast, plastic cards with opaque/coloured areas and unique features not seen on everyday paper business cards. It would be nice to see a few different colour combinations, we are open to new ideas so please feel free to take some artistic licence.
Should not have
• Must not be too busy, difficult to read or be distracting from the information conveyed. Other than this please feel free to add your own touches and make it unique!

```html
<!DOCTYPE html>
<html lang="en">
<head>
<meta charset="utf-8">
<title>Harlow Ridge Builders – Business Card</title>
<link rel="stylesheet" href="https://fonts.googleapis.com/css2?family=Libre+Baskerville:wght@400;700&family=Open+Sans:wght@400&display=swap">
<style>
  :root {
    --stage: #3b3b3b;
    --card-white: #f1f1f1;
    --ink: #1a1a1a;
    --ink-soft: #333333;
    --gold: #c09e2a;
    --gold-text: #c29b22;
    --white: #ffffff;
  }
  * { margin: 0; padding: 0; box-sizing: border-box; }
  html, body {
    width: 1200px; height: 750px; overflow: hidden;
    background: var(--stage);
  }
  .canvas { position: relative; width: 1200px; height: 750px; }
  .card {
    position: absolute; top: 228px;
    width: 462px; height: 263px;
  }
  .card-front { left: 124px; background: var(--card-white); }
  .card-back { left: 618px; background: var(--gold); }

  .brand {
    position: absolute; left: 28px; top: 40px;
    display: flex; align-items: center; gap: 10px;
    font-family: "Libre Baskerville", serif; font-weight: 400;
    color: var(--ink); font-size: 22px; line-height: 1.15;
  }
  .brand-mark { width: 14px; height: 14px; background: var(--gold); flex: none; }

  .person {
    position: absolute; right: 29px; top: 153px; text-align: right;
    font-family: "Libre Baskerville", serif;
  }
  .person-name { font-weight: 700; font-size: 18px; color: var(--ink); letter-spacing: 0.3px; }
  .person-role { font-size: 12.5px; color: var(--gold-text); margin-top: 1px; }

  .edge-tab { position: absolute; right: 0; top: 154px; width: 12px; height: 40px; }

  .divider {
    position: absolute; left: 28px; top: 196px;
    width: 403px; height: 1px; background: var(--ink-soft);
  }

  .contacts {
    position: absolute; top: 207px;
    font-family: "Open Sans", sans-serif; font-size: 10.5px; color: var(--ink-soft);
    list-style: none;
  }
  .contacts li { display: flex; align-items: center; height: 17.5px; gap: 6px; }
  .contacts-phone { left: 28px; }
  .contacts-web { right: 29px; }
  .contacts-web li { justify-content: flex-end; }
  .icon { width: 11px; height: 11px; flex: none; fill: var(--ink); }

  .back-brand {
    position: absolute; right: 31px; top: 170px;
    display: flex; align-items: center; gap: 10px;
    font-family: "Libre Baskerville", serif; font-weight: 400;
    font-size: 20px; color: var(--white);
  }
  .back-brand .brand-mark { background: var(--white); width: 12px; height: 12px; }
  .back-url {
    position: absolute; right: 31px; top: 220px;
    font-family: "Open Sans", sans-serif; font-size: 10.5px;
    letter-spacing: 5px; color: var(--white);
  }
</style>
</head>
<body>
<main class="canvas">
  <section class="card card-front" aria-label="Card front">
    <div class="brand">
      <span class="brand-mark"></span>
      <span>Harlow Ridge<br>Builders</span>
    </div>

    <div class="person">
      <div class="person-name">Callum Whitford</div>
      <div class="person-role">Managing Director</div>
    </div>

    <svg class="edge-tab" viewBox="0 0 12 40" aria-hidden="true">
      <polygon points="0,5 12,0 12,40 0,35" fill="var(--gold)"/>
    </svg>

    <div class="divider"></div>

    <ul class="contacts contacts-phone">
      <li>
        <svg class="icon" viewBox="0 0 24 24" aria-hidden="true"><path d="M6.6 10.8a15.1 15.1 0 0 0 6.6 6.6l2.2-2.2c.3-.3.7-.4 1-.2 1.1.4 2.3.6 3.6.6.6 0 1 .4 1 1V20c0 .6-.4 1-1 1A17 17 0 0 1 3 4c0-.6.4-1 1-1h3.5c.6 0 1 .4 1 1 0 1.3.2 2.5.6 3.6.1.3 0 .7-.2 1z"/></svg>
        <span>0400 317 852</span>
      </li>
      <li>
        <svg class="icon" viewBox="0 0 24 24" aria-hidden="true"><path d="M7 1h10a2 2 0 0 1 2 2v18a2 2 0 0 1-2 2H7a2 2 0 0 1-2-2V3a2 2 0 0 1 2-2zm0 3v14h10V4z"/></svg>
        <span>(02) 55 501 846</span>
      </li>
    </ul>

    <ul class="contacts contacts-web">
      <li>
        <span>harlowridge@northmail.com</span>
        <svg class="icon" viewBox="0 0 24 24" aria-hidden="true"><path d="M2 5h20v14H2zm2 2v.5l8 5 8-5V7l-8 5z"/></svg>
      </li>
      <li>
        <span>www.northmail.com</span>
        <svg class="icon" viewBox="0 0 24 24" aria-hidden="true"><circle cx="12" cy="12" r="10"/><path d="M7 8c2 0 3 1 3 3s-2 2-2 4M15 5c-1 2 1 3 3 3M14 14c1 1 2 3 1 5" stroke="#fff" stroke-width="1.6" fill="none"/></svg>
      </li>
    </ul>
  </section>

  <section class="card card-back" aria-label="Card back">
    <div class="back-brand">
      <span class="brand-mark"></span>
      <span>Harlow Ridge Builders</span>
    </div>
    <div class="back-url">www.northmail.com</div>
  </section>
</main>
</body>
</html>
```